Wordpress Design Project plorn.ie

We want to setup a new WP site for a VANTERLY USER group in Ireland. We hae the logo and a short intro video
We want to be able to blog and post videos (u tube links) to the page.

If you look at the image below *plorn site this is a try we made, but have run out of time.

Target Market(s)

Techies and mostly bouring men like us.

Industry/Entity Type

Group

Requirements
Must have
• 4 pages, Simple Clean and easy to nivagate and easy for us to use.

Explore
Plan
Deploy
Configure

have a look at - http://www.plorn.be/ We do not want an exact copy of
Nice to have
• Login
down load section
link to other blogs etc
social netwrok links FB,Pintrest etc
about us

```html
<!DOCTYPE html>
<html lang="en">
<head>
<meta charset="utf-8">
<title>PLORN.IE – Fleet Console User Group Ireland</title>
<link rel="stylesheet" href="https://fonts.googleapis.com/css2?family=Arimo:wght@400;700&family=PT+Sans:wght@400;700&display=swap">
<style>
:root{
  --ink:#3a3a3a;
  --ink-soft:#555;
  --muted:#9a9a9a;
  --line:#e3e3e3;
  --green:#6cbf3a;
  --green-dark:#4fa62a;
  --orange:#f39315;
  --orange-dark:#e07d05;
  --hero-top:#e9e9e9;
  --hero-bottom:#d4d4d4;
  --white:#fff;
}
*{box-sizing:border-box;margin:0;padding:0}
html,body{width:1200px;height:851px;overflow:hidden;background:var(--white)}
body{font-family:"PT Sans",Arial,sans-serif;color:var(--ink);position:relative}
a{text-decoration:none;color:inherit}

/* header */
.site-header{position:absolute;left:0;top:0;width:1200px;height:107px}
.brand{position:absolute;left:118px;top:32px;display:flex;align-items:center;gap:12px}
.brand-name{font-size:36px;font-weight:400;color:#222;letter-spacing:1px;line-height:1}
.brand-mark{width:22px;height:22px;border-radius:50%;background:var(--green)}
.lang{position:absolute;left:744px;top:33px;font-size:12px;color:var(--ink-soft);display:flex;align-items:center;gap:6px}
.lang .caret{font-size:8px;margin-left:4px}
.search{position:absolute;left:884px;top:26px;width:194px;height:27px;border:1px solid #ddd;border-radius:3px;font-size:11px;font-style:italic;color:#c4c4c4;padding:7px 10px}
.main-nav{position:absolute;left:538px;top:66px;display:flex}
.main-nav a{font-size:14px;color:#777;height:41px;padding:11px 0 0;text-align:center}
.main-nav a.current{color:#333;border-bottom:3px solid var(--green)}
.btn-small{position:absolute;top:72px;height:20px;border-radius:3px;color:#fff;font-size:11px;line-height:20px;text-align:center}
.btn-signup{left:947px;width:57px;background:linear-gradient(#f9a531,var(--orange-dark))}
.btn-signin{left:1016px;width:61px;background:linear-gradient(#6fc13e,var(--green-dark))}

/* hero */
.hero{position:absolute;left:0;top:107px;width:1200px;height:291px;background:linear-gradient(170deg,var(--hero-top),var(--hero-bottom))}
.hero-title{position:absolute;left:118px;top:48px;font-family:"Arimo",Arial,sans-serif;font-size:30px;font-weight:400;color:#444;letter-spacing:-0.5px}
.hero-title strong{font-weight:700}
.hero-text{position:absolute;left:119px;top:97px;width:530px;font-size:13.5px;line-height:18px;color:#555}
.btn-explore{position:absolute;left:118px;top:188px;width:144px;height:34px;border-radius:4px;background:linear-gradient(#fba524,var(--orange-dark));color:#fff;font-family:"Arimo",Arial,sans-serif;font-weight:700;font-size:15px;line-height:34px;padding-left:13px;box-shadow:0 2px 3px rgba(0,0,0,.2)}
.btn-explore::after{content:"";position:absolute;right:18px;top:13px;border-left:5px solid #fff;border-top:4px solid transparent;border-bottom:4px solid transparent}
.hero-device{position:absolute;left:668px;top:36px;width:348px;height:234px;border-radius:8px;background:linear-gradient(#2c3a28 0 68%,#e4e4e4 68% 100%)}
.hero-pointer{position:absolute;left:212px;top:281px;border-bottom:10px solid var(--white);border-left:11px solid transparent;border-right:11px solid transparent}

/* section tabs */
.sections{position:absolute;left:118px;top:430px;width:960px;height:80px;display:flex}
.section{position:relative;width:240px;display:flex;gap:20px;padding-left:28px;padding-top:4px}
.section + .section{border-left:1px solid var(--line)}
.section:nth-child(2){padding-left:32px}
.section h2{font-family:"Arimo",Arial,sans-serif;font-weight:400;font-size:18px;color:var(--muted);line-height:22px}
.section p{font-size:13.5px;color:#aaa;margin-top:3px}
.section.current h2{color:#222}
.section.current p{color:#444}
.section svg{flex:none}
.sections-rule{position:absolute;left:82px;top:510px;width:980px;height:1px;background:var(--line)}

/* content */
.video{position:absolute;left:118px;top:549px;width:281px;height:138px;border-radius:4px;background:radial-gradient(ellipse at center,#fafafa 30%,#d6d6d6 100%)}
.video .play{position:absolute;left:114px;top:39px}
.video-label{position:absolute;left:0;top:91px;width:100%;text-align:center;font-family:"Arimo",Arial,sans-serif;font-size:13px;color:#444;letter-spacing:-0.3px}
.video-label strong{font-weight:700}
.video-note{position:absolute;left:119px;top:696px;font-size:13.5px;color:#555}
.accent{color:var(--orange)}
.col-title{position:absolute;font-family:"Arimo",Arial,sans-serif;font-weight:400;font-size:17px;color:#444;letter-spacing:-0.3px}
.col-title strong{font-weight:700}
.downloads-title{left:458px;top:547px}
.downloads{position:absolute;left:458px;top:580px;width:300px;list-style:none}
.downloads li{position:relative;padding-left:18px;font-size:13.5px;line-height:18px;color:#555;margin-bottom:6px}
.downloads li::before{content:"";position:absolute;left:0;top:6px;border-left:4px solid #888;border-top:3px solid transparent;border-bottom:3px solid transparent}
.downloads-link{position:absolute;left:476px;top:666px;font-size:13.5px}
.connect-title{left:802px;top:547px}
.social{position:absolute;left:802px;top:586px;display:flex;gap:23px}
.social span{width:23px;height:23px;border-radius:50%;background:#666;display:block}

/* footer */
.footer-rule{position:absolute;left:118px;top:763px;width:960px;height:1px;background:var(--line)}
.footer-links{position:absolute;left:0;top:785px;width:1200px;text-align:center;font-size:11.5px;color:#444}
.footer-links .sep{color:#bbb;margin:0 6px}
.copyright{position:absolute;left:0;top:807px;width:1200px;text-align:center;font-size:11.5px;color:#444}
</style>
</head>
<body>

<header class="site-header">
  <a class="brand" href="#"><span class="brand-name">PLORN.IE</span><span class="brand-mark"></span></a>
  <div class="lang">
    <svg width="14" height="9" viewBox="0 0 3 2" aria-hidden="true"><rect width="1" height="2" fill="#169b62"/><rect x="1" width="1" height="2" fill="#fff"/><rect x="2" width="1" height="2" fill="#ff883e"/></svg>
    Ireland Language <span class="caret">▼</span>
  </div>
  <div class="search">Search keyword</div>
  <nav class="main-nav">
    <a class="current" href="#" style="width:62px">Home</a>
    <a href="#" style="width:94px">Features</a>
    <a href="#" style="width:68px">Plugins</a>
    <a href="#" style="width:96px">Tutorials</a>
    <a href="#" style="width:62px">Fltcnsl</a>
  </nav>
  <a class="btn-small btn-signup" href="#">Sign Up</a>
  <a class="btn-small btn-signin" href="#">Sign In ▸</a>
</header>

<section class="hero">
  <h1 class="hero-title"><strong>Explore</strong> Fleet Console</h1>
  <p class="hero-text">Lorem ipsum dolor sit amet, consectetuer adipiscing elit, sed diam nonummy nibh euismod tincidunt ut laoreet dolore magna aliquam erat volutpat. Ut wisi enim ad minim veniam, quis nostrud exerci tation ullamcorper suscipit lobortis nisl ut aliquip ex ea commodo consequat.</p>
  <a class="btn-explore" href="#">Explore Now</a>
  <div class="hero-device" role="img" aria-label="Tablet with attached keyboard showing the PLORN.IE name on a green screen"></div>
  <span class="hero-pointer"></span>
</section>

<div class="sections">
  <div class="section current">
    <svg width="32" height="30" viewBox="0 0 32 30" aria-hidden="true"><path d="M1 3h11l3 3h16v4H1z" fill="#111"/><path d="M1 12h30v17H1z" fill="#111"/></svg>
    <div><h2>Explore</h2><p>Explore Fleet Console</p></div>
  </div>
  <div class="section">
    <svg width="32" height="32" viewBox="0 0 32 32" aria-hidden="true" fill="#999"><path d="M16 2 31 9 16 16 1 9z"/><path d="M4 14 16 20 28 14 31 16 16 23 1 16z"/><path d="M4 21 16 27 28 21 31 23 16 30 1 23z"/></svg>
    <div><h2>Plan</h2><p>Plan Fleet Console</p></div>
  </div>
  <div class="section">
    <svg width="32" height="32" viewBox="0 0 32 32" aria-hidden="true"><path d="M16 1 31 8 16 15 1 8z" fill="#aaa"/><path d="M1 10 15 17v14L1 24z" fill="#888"/><path d="M31 10 17 17v14l14-7z" fill="#999"/></svg>
    <div><h2>Deploy</h2><p>Deploy Fleet Console</p></div>
  </div>
  <div class="section">
    <svg width="32" height="32" viewBox="0 0 32 32" aria-hidden="true"><g fill="#999"><circle cx="16" cy="16" r="11"/><rect x="13" y="1" width="6" height="30"/><rect x="1" y="13" width="30" height="6"/><rect x="13" y="1" width="6" height="30" transform="rotate(45 16 16)"/><rect x="13" y="1" width="6" height="30" transform="rotate(-45 16 16)"/></g><circle cx="16" cy="16" r="5" fill="#fff"/></svg>
    <div><h2>Configure</h2><p>Configure Fleet Console</p></div>
  </div>
</div>
<div class="sections-rule"></div>

<div class="video">
  <svg class="play" width="46" height="46" viewBox="0 0 46 46" aria-hidden="true"><circle cx="23" cy="23" r="23" fill="#5a5a5a"/><path d="M18 14 31 23 18 32z" fill="#fff"/></svg>
  <div class="video-label"><strong>Demo</strong> Information</div>
</div>
<p class="video-note">View PLORN Community in <a class="accent" href="#">Clipstream</a></p>

<h3 class="col-title downloads-title"><strong>Downloads</strong> Center</h3>
<ul class="downloads">
  <li>Lorem ipsum dolor sit amet, consectetuer adipiscing elit, sed diam nonummy nibh.</li>
  <li>Ut wisi enim ad minim veniam, quis nostrud exerci tation ullamcorper</li>
</ul>
<a class="downloads-link accent" href="#">View all downloads</a>

<h3 class="col-title connect-title"><strong>Other</strong> Ways to Connect</h3>
<div class="social"><span></span><span></span><span></span><span></span></div>

<div class="footer-rule"></div>
<nav class="footer-links">
  <a href="#">Legal Notice</a><span class="sep">•</span><a href="#">Terms of Service</a><span class="sep">•</span><a href="#">Privacy</a><span class="sep">•</span><a href="#">About PLORN</a><span class="sep">•</span><a href="#">Help</a><span class="sep">•</span><a href="#">FAQ</a>
</nav>
<p class="copyright">© 2012 PLORN.IE. All rights reserved.</p>

</body>
</html>
```